BrightKeel Business Card Contest

We are looking for a modern business card that catches attention and is unique. Attached is the brand guide and logo files. Please note that the back side (not the side with our name and info) with be UV raise printed, so have fun with the design there. We want to include Name, Title, Phone number, email, website.

Contact Information for Business Card

Please see project description

```html
<!DOCTYPE html>
<html lang="en">
<head>
<meta charset="UTF-8">
<title>BrightKeel Business Card</title>
<link href="https://fonts.googleapis.com/css2?family=Montserrat:wght@500;600&family=Open+Sans:ital,wght@0,400;1,400&display=swap" rel="stylesheet">
<style>
  :root {
    --backdrop: #1a1a1c;
    --charcoal-light: #474a51;
    --charcoal-dark: #25272c;
    --navy-light: #4d5080;
    --navy-dark: #1f2662;
    --sky-light: #45bde8;
    --sky-dark: #2490c4;
    --ember: #e8452e;
    --amber: #f4962c;
    --ice: #c9d6e4;
    --cyan: #36c8ec;
    --cobalt: #2a5fae;
    --white: #ffffff;
    --url-grey: #a9b4c2;
  }
  * { margin: 0; padding: 0; box-sizing: border-box; }
  html, body { width: 1200px; height: 916px; overflow: hidden; background: var(--backdrop); }
  body { position: relative; font-family: "Open Sans", sans-serif; }

  .card {
    position: absolute;
    left: 300px;
    width: 600px;
    height: 343px;
    overflow: hidden;
    box-shadow: 0 10px 30px rgba(0,0,0,.55);
  }

  /* Back side */
  .card-back {
    top: 70px;
    background: linear-gradient(135deg, var(--navy-light) 0%, var(--navy-dark) 60%, #1c2358 100%);
    display: flex;
    align-items: center;
    justify-content: center;
  }
  .back-brand {
    display: flex;
    align-items: center;
    gap: 16px;
  }
  .brand-square {
    width: 34px;
    height: 34px;
    background: var(--cyan);
  }
  .back-brand .brand-name {
    font-family: "Montserrat", sans-serif;
    font-weight: 600;
    font-size: 44px;
    color: var(--white);
    letter-spacing: .5px;
  }

  /* Front side */
  .card-front {
    top: 493px;
    background: radial-gradient(ellipse at 35% 70%, var(--charcoal-light) 0%, var(--charcoal-dark) 75%);
  }
  .edge-stripe {
    position: absolute;
    left: 26px;
    top: 22px;
    width: 4px;
    height: 240px;
    background: linear-gradient(180deg, var(--ember) 0%, var(--amber) 12%, var(--ice) 35%, var(--cyan) 65%, var(--cobalt) 100%);
  }
  .front-brand {
    position: absolute;
    left: 60px;
    top: 128px;
    width: 250px;
    display: flex;
    flex-direction: column;
    align-items: center;
    gap: 14px;
  }
  .front-brand .brand-square { width: 30px; height: 30px; }
  .front-brand .brand-name {
    font-family: "Montserrat", sans-serif;
    font-weight: 600;
    font-size: 40px;
    color: var(--white);
  }
  .website {
    position: absolute;
    left: 56px;
    top: 286px;
    font-style: italic;
    font-size: 15px;
    letter-spacing: 7px;
    color: var(--url-grey);
  }

  .info-panel {
    position: absolute;
    left: 345px;
    top: 24px;
    width: 230px;
    height: 276px;
    background: linear-gradient(160deg, var(--sky-light) 0%, #4bb6dd 55%, var(--sky-dark) 100%);
  }
  .info-panel::before {
    content: "";
    position: absolute;
    left: 0;
    top: 0;
    width: 4px;
    height: 100%;
    background: linear-gradient(180deg, var(--ember) 0%, var(--amber) 12%, var(--ice) 35%, var(--cyan) 65%, var(--cobalt) 100%);
  }
  .person-name {
    position: absolute;
    left: 24px;
    top: 18px;
    font-family: "Montserrat", sans-serif;
    font-weight: 600;
    font-size: 19px;
    color: var(--white);
  }
  .person-title {
    position: absolute;
    left: 24px;
    top: 44px;
    font-style: italic;
    font-size: 11px;
    color: var(--white);
  }
  .contact-list {
    position: absolute;
    left: 18px;
    bottom: 22px;
    list-style: none;
    display: flex;
    flex-direction: column;
    gap: 8px;
  }
  .contact-item {
    display: flex;
    align-items: center;
    gap: 8px;
    font-size: 13px;
    color: var(--white);
  }
  .contact-icon { width: 18px; height: 18px; flex: none; }
</style>
</head>
<body>

  <section class="card card-back" aria-label="Card back">
    <div class="back-brand">
      <span class="brand-square"></span>
      <span class="brand-name">BrightKeel</span>
    </div>
  </section>

  <section class="card card-front" aria-label="Card front">
    <span class="edge-stripe"></span>

    <div class="front-brand">
      <span class="brand-square"></span>
      <span class="brand-name">BrightKeel</span>
    </div>
    <p class="website">www.brightkeel.com</p>

    <div class="info-panel">
      <h1 class="person-name">Daria Novak</h1>
      <p class="person-title">Director</p>

      <ul class="contact-list">
        <li class="contact-item">
          <svg class="contact-icon" viewBox="0 0 18 18" aria-hidden="true">
            <circle cx="9" cy="9" r="9" fill="#f0a83a"/>
            <path d="M5.5 5.2c.4-.4 1-.4 1.3 0l.9 1.1c.3.4.3.9-.1 1.2l-.5.4c.5 1.1 1.4 2 2.5 2.5l.4-.5c.3-.4.8-.4 1.2-.1l1.1.9c.4.3.4.9 0 1.3l-.6.6c-.5.5-1.3.6-1.9.3-2-1-3.5-2.5-4.5-4.5-.3-.6-.2-1.4.3-1.9z" fill="#fff"/>
          </svg>
          +00 555 010 274
        </li>
        <li class="contact-item">
          <svg class="contact-icon" viewBox="0 0 18 18" aria-hidden="true">
            <circle cx="9" cy="9" r="9" fill="#f0a83a"/>
            <rect x="4.5" y="5.8" width="9" height="6.4" rx=".8" fill="#fff"/>
            <path d="M4.8 6.2L9 9.4l4.2-3.2" fill="none" stroke="#f0a83a" stroke-width="1"/>
          </svg>
          hello@brightkeel.com
        </li>
      </ul>
    </div>
  </section>

</body>
</html>
```